Land Buying Company Needs Letterhead for Direct Mail Marketing to Land Owners

We are looking for a professional letterhead that we will be including in our direct mail marketing. We will be sending this to land owners who may be interested in selling or purchasing land.

The letterhead needs to be editable. Headers and footers would look nice, but we are open. We would want it to include our address, website, phone, and email info. For right now the address to use for design purposes would the following:

Address: 415 Bramwell Avenue #600
Dallas, TX 75219
Website - www.quillridgeacres.example
Email - info@quillridgeacres.example
Phone - 866-402-ACRE

I have attached our logo zip file that we just had done on Pixel Guild. Let me know what questions you have, and thank you.

```html
<!DOCTYPE html>
<html lang="en">
<head>
<meta charset="utf-8">
<title>Quillridge Acres Letterhead</title>
<link rel="stylesheet" href="https://fonts.googleapis.com/css2?family=Montserrat:ital,wght@0,500;0,600;0,700;1,700&family=PT+Sans+Narrow:wght@400;700&display=swap">
<style>
  :root {
    --backdrop: #d9d9d9;
    --paper: #ffffff;
    --brand-green: #7dc142;
    --brand-dark: #3d5a1e;
    --ink: #4a4a4a;
    --ink-soft: #5a5a5a;
    --tree-tint: #ecece8;
  }
  * { box-sizing: border-box; margin: 0; padding: 0; }
  html, body { width: 1200px; height: 1067px; overflow: hidden; }
  body { background: var(--backdrop); position: relative; font-family: "PT Sans Narrow", sans-serif; }

  .letterhead {
    position: absolute; left: 242px; top: 28px;
    width: 715px; height: 1010px;
    background: var(--paper); overflow: hidden;
  }

  .brand { position: absolute; left: 66px; top: 61px; display: flex; align-items: center; gap: 10px; }
  .brand-dot { width: 55px; height: 55px; border-radius: 50%; background: var(--brand-dark); }
  .brand-name {
    font-family: "Montserrat", sans-serif; font-weight: 600; font-size: 22px;
    color: var(--brand-green); letter-spacing: 0.5px; text-transform: uppercase;
  }

  .header-divider { position: absolute; left: 383px; top: 50px; width: 2px; height: 76px; background: var(--brand-green); opacity: .8; }

  .contact { position: absolute; left: 439px; top: 50px; font-family: "Montserrat", sans-serif; font-weight: 500; font-size: 11.5px; color: var(--ink); line-height: 15px; }
  .contact-address { margin-bottom: 9px; }
  .contact-line { display: flex; align-items: center; gap: 5px; }
  .contact-line svg { width: 8px; height: 8px; flex: none; }

  .greeting { position: absolute; left: 66px; top: 296px; font-family: "Montserrat", sans-serif; font-weight: 600; font-size: 18px; color: var(--ink); }

  .letter-body { position: absolute; left: 66px; top: 338px; width: 584px; color: var(--ink-soft); font-size: 11.5px; line-height: 18.2px; text-align: justify; }
  .letter-body p + p { margin-top: 18px; }

  .sign-off { position: absolute; left: 66px; top: 706px; font-family: "Montserrat", sans-serif; color: var(--ink); }
  .sign-name { font-size: 19px; font-weight: 700; font-style: italic; line-height: 22px; }
  .sign-role { font-size: 10px; font-weight: 700; font-style: italic; }

  .signature { position: absolute; left: 66px; top: 768px; width: 184px; height: 66px; background: linear-gradient(90deg, #e3e3e3, #cfcfcf); border-radius: 4px; z-index: 2; }

  .tree-band { position: absolute; left: 0; bottom: 0; width: 715px; height: 316px; background: linear-gradient(180deg, rgba(236,236,232,0) 0%, var(--tree-tint) 45%, var(--tree-tint) 100%); }
</style>
</head>
<body>
  <main class="letterhead">
    <div class="tree-band" role="img" aria-label="Faint pale grey pine tree silhouettes along the bottom of the page"></div>

    <header>
      <div class="brand">
        <span class="brand-dot"></span>
        <span class="brand-name">Quillridge Acres</span>
      </div>
      <div class="header-divider"></div>
      <address class="contact" style="font-style:normal">
        <div class="contact-address">415 Bramwell Avenue #600<br>Dallas, TX 75219</div>
        <div class="contact-line">
          <svg viewBox="0 0 8 8"><path d="M1.5 0.5l1.5 0 .5 2-1 .8a4 4 0 0 0 2.2 2.2l.8-1 2 .5v1.5c0 .5-.5 1-1 1A6.5 6.5 0 0 1 .5 1.5c0-.5.5-1 1-1z" fill="#7dc142"/></svg>
          866-402-ACRE
        </div>
        <div class="contact-line">
          <svg viewBox="0 0 8 8"><rect x="0.5" y="1.5" width="7" height="5" rx="0.6" fill="none" stroke="#7dc142"/><path d="M0.8 1.8L4 4.3 7.2 1.8" fill="none" stroke="#7dc142" stroke-width=".8"/></svg>
          info@quillridgeacres.example
        </div>
        <div class="contact-line">
          <svg viewBox="0 0 8 8"><circle cx="4" cy="4" r="3.4" fill="#7dc142"/></svg>
          www.quillridgeacres.example
        </div>
      </address>
    </header>

    <h1 class="greeting">Dear sir/Madam,</h1>

    <section class="letter-body">
      <p>Lorem Ipsum is simply dummy text of the printing and typesetting industry. Lorem Ipsum has been the industry's standard dummy text ever since the 1500s, when an unknown printer took a galley of type and scrambled it to make a type specimen book. It has survived not only five centuries, but also the leap into electronic typesetting, remaining essentially unchanged. It was popularised in the 1960s with the release of Typeset</p>
      <p>Contrary to popular belief, Lorem Ipsum is not simply random text. It has roots in a piece of classical Latin literature from 45 BC, making it over 2000 years old. Roland Whitcombe, a Latin professor at Ashford College in Virginia, looked up one of the more obscure Latin words, consectetur, from a Lorem Ipsum passage, and going through the cites of the word in classical literature, discovered the undoubtable source. Lorem Ipsum comes from sections 1.10.32 and 1.10.33 of "de Finibus Bonorum et Malorum" (The Extremes of Good and Evil) by Varro, written in 45 BC. This book is a treatise on the theory of ethics, very popular during the Renaissance. The first line of Lorem Ipsum, "Lorem ipsum dolor sit amet..", comes from a line in section 1.10.32. typesetting, remaining essentially unchanged. It was popularised in the 1960s with the release of Typeset sheets containing Lorem Ipsum passages, and more recently with desktop publishing software like Folio Page There are many variations of passages of Lorem Ipsum available, but the majority have suffered alteration in</p>
      <p>some form, by injected humour, or randomised words which don't look even slightly believable. If you are going to use a passage of Lorem Ipsum, you need to be sure there isn't anything embarrassing hidden in the middle</p>
    </section>

    <div class="sign-off">
      <div class="sign-name">Daniel Harlow</div>
      <div class="sign-role">Director</div>
    </div>
    <div class="signature" role="img" aria-label="Handwritten signature of the director"></div>
  </main>
</body>
</html>
```